Zielgruppe
Die travlon GmbH bietet professionelle Cloud-Lösungen im Bereich spezialisierter Verwaltungssysteme. Hierbei handelt es sich um Software as a Service (SaaS), die zu 100% von der travlon GmbH betrieben und kontinuierlich weiterentwickelt wird.
Aufgabenstellung
Das Design kann Farben und/oder Elemente der travlon GmbH enthalten (www.travlon.de). Da es sich um ein eigenen Produkt handelt, muss jedoch auch Neutralität bewahrt werden.

```html
<!DOCTYPE html>
<html lang="de">
<head>
<meta charset="utf-8">
<title>travlon – Domains auflisten</title>
<link href="https://fonts.googleapis.com/css2?family=Lato:wght@400;700&display=swap" rel="stylesheet">
<style>
:root{
  --red:#d0033c;
  --ink:#3b4550;
  --muted:#6b7682;
  --line:#c9ced4;
  --soft:#eef0f2;
  --tab:#aab7c3;
  --btn-grey:#aebcca;
  --green:#7cb342;
  --orange:#f47b3a;
  --white:#fff;
  --bg-light:#bfc8d0;
  --bg-dark:#566b83;
}
*{box-sizing:border-box;margin:0;padding:0}
html,body{width:1200px;height:990px;overflow:hidden}
body{font-family:'Lato',sans-serif;color:var(--ink);position:relative;background:var(--bg-light)}
.backdrop{position:absolute;left:0;top:66px;width:1200px;height:924px;background:linear-gradient(30deg,var(--bg-light) 0%,#93a4b5 55%,var(--bg-dark) 100%)}
.abs{position:absolute}
/* header */
.topbar{position:absolute;left:0;top:0;width:1200px;height:66px;background:var(--white)}
.brand{position:absolute;left:151px;top:7px;display:flex;align-items:flex-end;gap:6px}
.brand-square{width:46px;height:50px;background:var(--red)}
.brand-name{font-size:24px;color:#222;line-height:1;margin-bottom:2px}
.meta{position:absolute;font-size:11.5px;color:var(--ink)}
.meta b{color:var(--red);font-weight:400}
.session-bar{position:absolute;left:845px;top:33px;width:107px;height:3px;background:#2ea043}
/* sidebar */
.sidebar{position:absolute;left:150px;top:103px;width:252px;height:512px;background:var(--white);padding:9px 20px 0 20px}
.sidebar li{list-style:none;height:33.2px;border-bottom:1px solid var(--line);font-size:12px;display:flex;align-items:center}
.sidebar li::before{content:"›";color:var(--red);width:13px;font-size:13px}
.sidebar li.sub::before{content:"–";width:31px;padding-left:17px}
/* tabs */
.tab{position:absolute;top:104px;width:111px;height:44px;background:var(--tab);font-weight:700;font-size:12px;display:flex;align-items:center;justify-content:center;color:#34404c;border-radius:3px 3px 0 0}
.tab.active{background:var(--red);color:var(--white)}
/* panel */
.panel{position:absolute;left:424px;top:147px;width:626px;height:770px;background:var(--white);font-size:11px}
.box{position:absolute;left:28px;width:575px;border:1px solid #d6dadf;border-radius:3px}
.box-head{height:25px;background:var(--soft);display:flex;align-items:center;padding:0 14px;font-weight:700;font-size:11px}
.box-head .right{margin-left:auto;font-weight:400;font-size:8.5px;display:flex;align-items:center;gap:8px}
.field{position:absolute;height:19px;border:1px solid #d6dadf;border-radius:10px;font-size:10.5px;padding:0 10px;display:flex;align-items:center;color:#aaa}
.field.val{color:var(--ink)}
.chev{margin-left:auto;width:6px;height:6px;border-right:1.2px solid #555;border-bottom:1.2px solid #555;transform:rotate(45deg);margin-top:-3px}
.label{position:absolute;font-size:11px;color:var(--muted)}
.q{display:inline-block;width:11px;height:11px;border-radius:50%;background:var(--red);color:#fff;font-size:8px;font-weight:700;text-align:center;line-height:11px;margin-right:8px}
.btn-red{position:absolute;background:var(--red);color:#fff;font-weight:700;font-size:11px;display:flex;align-items:center;justify-content:center;border-radius:2px}
.sort{position:absolute;left:42px;top:379px;width:542px;height:24px;border:1px solid var(--line);display:flex;font-size:10.5px}
.sort span{border-right:1px solid var(--line);display:flex;align-items:center;padding:0 0 0 15px;gap:5px}
.sort span:last-child{border:0}
.arr{color:#8a96a2}
.arr i{font-style:normal;color:var(--green)}
.row{position:absolute;left:42px;width:542px;height:20px;display:flex;align-items:center;font-size:9.5px}
.dot{width:8px;height:8px;border-radius:50%;background:#777;margin-right:3.5px}
.dot.g{background:var(--green)}
.chk{width:9px;height:9px;border:1px solid #aaa;margin-left:4px}
.pill{position:absolute;height:14px;background:var(--btn-grey);color:#fff;font-size:7.5px;display:flex;align-items:center;justify-content:center}
.sep{position:absolute;left:42px;width:542px;height:1px;background:#d6dadf}
</style>
</head>
<body>
<div class="backdrop" role="img" aria-label="Dekorativer Hintergrund in Grau-, Blau- und Rottönen"></div>

<header class="topbar">
  <div class="brand"><div class="brand-square"></div><span class="brand-name">travlon</span></div>
  <div class="meta" style="left:482px;top:19px">✉&nbsp; neue Nachrichten: <b>6</b></div>
  <div class="meta" style="left:482px;top:37px">☰&nbsp; Auftragsstapel: &nbsp;&nbsp;&nbsp;<b>0</b></div>
  <div class="meta" style="left:646px;top:24px">Version: 2.2.7</div>
  <div class="meta" style="left:735px;top:24px">⊞&nbsp; Sitemap</div>
  <div class="meta" style="left:835px;top:17px">angemeldet als marlene</div>
  <div class="session-bar"></div>
  <div class="meta" style="left:862px;top:40px">118 min. Restzeit</div>
  <div class="meta" style="left:994px;top:25px">Logout <b>⏻</b></div>
</header>

<ul class="sidebar">
  <li>Domain-Liste</li><li>Domain registrieren</li><li>Domain transferieren</li>
  <li>Domain bearbeiten</li><li>Domain wiederherstellen</li><li>Massenauftrage</li>
  <li>DNSSEC</li><li class="sub">DNSSEC-Liste</li><li class="sub">DNSSEC erstellen</li>
  <li class="sub">DNSSEC Info</li><li>Werkzeuge</li><li class="sub">Whois</li>
  <li class="sub">Puny-Kodierung</li><li class="sub">Zonecheck</li>
</ul>

<div class="tab" style="left:435px">START</div>
<div class="tab" style="left:554px">BENUTZER</div>
<div class="tab" style="left:674px">KONTAKT</div>
<div class="tab active" style="left:794px">DOMAIN</div>
<div class="tab" style="left:914px">DNS</div>

<main class="panel">
  <div class="abs" style="left:27px;top:32px;font-size:12px">Domains auflisten</div>
  <div class="abs" style="left:507px;top:32px;font-size:12px"><span class="q">–</span>Zurucksetzen</div>

  <section class="box" style="top:57px;height:163px">
    <div class="box-head">Listen-Filter
      <span class="right">Zeilen pro Seite <span class="field" style="position:static;width:72px;height:15px;font-size:8px">-<i class="chev"></i></span> Weitere Optionen <span style="border:1px solid #999;width:10px;height:10px;display:inline-flex;align-items:center;justify-content:center">+</span></span>
    </div>
  </section>
  <div class="label" style="left:42px;top:98px"><span class="q">?</span>Domain:</div>
  <div class="field" style="left:147px;top:96px;width:150px">*</div>
  <div class="label" style="left:337px;top:98px"><span class="q">?</span>Umlautdomain:</div>
  <div class="field" style="left:441px;top:96px;width:151px">*</div>

  <div class="label" style="left:42px;top:123px"><span class="q">?</span>Benutzer:</div>
  <div class="field val" style="left:147px;top:121px;width:126px">marlene<i class="chev"></i></div>
  <div class="abs" style="left:278px;top:121px;font-size:12px">⌕</div>
  <div class="label" style="left:337px;top:123px"><span class="q">?</span>Kontakt:</div>
  <div class="field" style="left:441px;top:121px;width:126px">*</div>
  <div class="abs" style="left:573px;top:121px;font-size:12px">⌕</div>

  <div class="label" style="left:61px;top:147px">Renewal-Mode:</div>
  <div class="field" style="left:147px;top:146px;width:126px">*<i class="chev"></i></div>
  <div class="label" style="left:337px;top:147px"><span class="q">?</span>Lock-Status:</div>
  <div class="field" style="left:441px;top:146px;width:126px">*<i class="chev"></i></div>

  <div class="label" style="left:42px;top:171px"><span class="q">?</span>Expire von:</div>
  <div class="field" style="left:147px;top:171px;width:126px">*</div>
  <div class="abs" style="left:278px;top:170px;font-size:11px;color:#666">▦</div>
  <div class="label" style="left:337px;top:171px"><span class="q">?</span>bis:</div>
  <div class="field" style="left:441px;top:171px;width:126px">*</div>
  <div class="abs" style="left:573px;top:170px;font-size:11px;color:#666">▦</div>
  <div class="abs" style="left:537px;top:195px;font-size:9.5px;color:var(--muted)">30 - 60 - 90</div>

  <div class="btn-red" style="left:221px;top:239px;width:185px;height:35px">Domains auflisten</div>

  <section class="box" style="top:295px;height:371px">
    <div class="box-head">Liste<span class="right">Export CSV <span style="border:1.5px solid #1d7a3a;color:#1d7a3a;width:13px;height:13px;display:inline-flex;align-items:center;justify-content:center;font-weight:700;font-size:9px">X</span></span></div>
  </section>
  <div class="abs" style="left:43px;top:338px;font-size:10.5px">3 Elemente</div>
  <div class="abs" style="left:159px;top:335px;font-size:13px">‹</div>
  <div class="field val" style="left:178px;top:336px;width:275px;font-size:8px;justify-content:flex-start;padding-left:16px">neuesdesign-beispielnetz.com - testdomain-beispielnetz.com<i class="chev"></i></div>
  <div class="abs" style="left:466px;top:335px;font-size:13px">›</div>
  <div class="abs" style="left:543px;top:338px;font-size:10.5px">Seite 1/1</div>

  <div class="sort">
    <span style="width:83px">Domain <b class="arr"><i>↑</i>↓</b></span>
    <span style="width:73px;padding-left:9px">Erstellt <b class="arr">↑↓</b></span>
    <span style="width:84px;padding-left:10px">Geandert <b class="arr">↑↓</b></span>
    <span style="width:71px;padding-left:10px">Expire <b class="arr">↑↓</b></span>
    <span style="width:96px;padding-left:8px">Nameserver <b class="arr">↑↓</b></span>
    <span style="padding-left:10px">Nameserver <b class="arr">↑↓</b></span>
  </div>

  <div class="abs" style="left:42px;top:417px;width:84px;height:24px;border:1px solid var(--line);font-size:10px;display:flex;align-items:center;padding-left:10px"><span style="color:var(--green);margin-right:6px">↓</span>Alle offnen</div>
  <div class="abs" style="left:42px;top:445px;width:542px;height:23px;border:1px solid var(--line);background:var(--soft);font-size:10px">
    <span class="abs" style="left:4px;top:3px;padding:2px 9px;border:1px solid var(--line);background:#fff">Status</span>
    <span class="abs" style="left:83px;top:0;height:21px;border-left:1px solid var(--line);padding:5px 0 0 11px">Domain</span>
    <span class="abs" style="left:474px;top:0;height:21px;border-left:1px solid var(--line);width:35px;text-align:center;padding-top:3px;font-size:13px;color:#888">↻</span>
    <span class="abs" style="left:509px;top:0;height:21px;border-left:1px solid var(--line);width:33px;text-align:center;padding-top:4px;color:#888">🔒︎</span>
  </div>

  <div class="row" style="top:481px"><i class="dot"></i><i class="dot"></i><i class="dot g"></i><i class="chk"></i><span style="margin-left:45px">neuesdesign-beispielnetz.com</span><span style="color:var(--orange);margin-left:5px">●</span>&nbsp;<span style="font-size:8px">NEU</span></div>
  <div class="pill" style="left:307px;top:484px;width:77px">✎ Vorlage laden</div>
  <div class="pill" style="left:395px;top:484px;width:55px">⌕ Historie</div>
  <span class="q abs" style="left:460px;top:485px">?</span>
  <div class="pill" style="left:475px;top:484px;width:42px">Whois</div>
  <div class="abs" style="left:528px;top:481px;color:var(--green);font-size:13px">✓</div>
  <div class="abs" style="left:563px;top:481px;color:var(--green);font-size:13px">✓</div>
  <div class="sep" style="top:514px"></div>

  <div class="row" style="top:526px"><i class="dot"></i><i class="dot"></i><i class="dot g"></i><i class="chk"></i><span style="margin-left:45px">neuesdesign-beispielnetz.com</span><span style="color:var(--orange);margin-left:5px">●</span>&nbsp;<span style="font-size:8px">NEU</span></div>
  <div class="pill" style="left:307px;top:529px;width:77px">✎ Vorlage laden</div>
  <div class="pill" style="left:395px;top:529px;width:55px">⌕ Historie</div>
  <span class="q abs" style="left:460px;top:530px">?</span>
  <div class="pill" style="left:475px;top:529px;width:42px">Whois</div>
  <div class="abs" style="left:528px;top:526px;color:var(--green);font-size:13px">✓</div>
  <div class="abs" style="left:563px;top:526px;color:var(--green);font-size:13px">✓</div>
  <div class="sep" style="top:559px"></div>

  <div class="row" style="top:570px"><i class="dot"></i><i class="dot"></i><i class="dot g"></i><i class="chk"></i><span style="margin-left:45px">neuesdesign-beispielnetz.com</span><span style="color:var(--orange);margin-left:5px">●</span>&nbsp;<span style="font-size:8px">NEU</span></div>
  <div class="pill" style="left:307px;top:573px;width:77px">✎ Vorlage laden</div>
  <div class="pill" style="left:395px;top:573px;width:55px">⌕ Historie</div>
  <span class="q abs" style="left:460px;top:574px">?</span>
  <div class="pill" style="left:475px;top:573px;width:42px">Whois</div>
  <div class="abs" style="left:528px;top:570px;color:var(--green);font-size:13px">✓</div>
  <div class="abs" style="left:563px;top:570px;color:var(--green);font-size:13px">✓</div>
  <div class="sep" style="top:603px"></div>

  <div class="abs" style="left:262px;top:626px;width:18px;height:18px;border:1px solid #ddd;text-align:center;font-size:12px;line-height:15px">‹</div>
  <div class="abs" style="left:297px;top:629px;font-size:10px">Seite 1/1</div>
  <div class="abs" style="left:355px;top:626px;width:18px;height:18px;border:1px solid #ddd;text-align:center;font-size:12px;line-height:15px">›</div>

  <svg class="abs" style="left:60px;top:625px" width="100" height="62" viewBox="0 0 100 62" aria-hidden="true">
    <path d="M95 58 C95 35 65 42 45 45 C25 48 12 40 12 18" fill="none" stroke="#9fb0c0" stroke-width="3"/>
    <path d="M2 22 L12 2 L22 22Z" fill="#9fb0c0"/>
  </svg>

  <div class="btn-red" style="left:142px;top:697px;width:140px;height:36px">Massenauftrag</div>
</main>
</body>
</html>
```